3 Sympathy Cards for Veterinary Hospital

Hi. Meadowbrook Pet Hospital is a Veterinary Hospital in Australia. We need sympathy cards to send to grieving clients after the loss of their beloved pets.
I have attached the old designs, but we have rebranded and need something to suit our new image.

The cards should have a nice message and appeal to every owner.
They need to match our current branding, but the cards are for the clients, not to advertise us, so not too much branding.
The current cards are attached and they are good because they show a variety of animals so clients might identify with one of them.
I have attached a brown to green gradient that we use on some designs, you don't have to use it, but consider it.
I have attached a logo on background used in some of our new designs, consider using it.
I have attached a font that we use for most new branding.

Target Market(s)

Women 25 to 44

Industry/Entity Type

Veterinary

Font styles to use
Sans Serif
Script

Colors
fac994
cadf82

Requirements
Must have
• IMPORTANT - 3 different designs for the different types of pets.
• 1. Dog.
• 2. Cat.
• 3. Everything else (Rabbits, lizards, ferrets, chickens, birds, mice, rats, snakes)
Nice to have
• Caring and compassionate message.
Should not have
• Too much branding.

```html
<!DOCTYPE html>
<html lang="en">
<head>
<meta charset="utf-8">
<title>Meadowbrook Pet Hospital – Sympathy Card</title>
<link rel="stylesheet" href="https://fonts.googleapis.com/css2?family=Arimo:wght@400;700&family=Lobster&display=swap">
<style>
  :root {
    --paper: #ffffff;
    --edge: #8a8a8a;
    --orange-text: #d68a42;
    --green-text: #4f8a34;
    --brand-brown: #7b5a3c;
    --wash-pale: #dbe2c3;
    --wash-green: #cde08a;
    --wash-peach: #f9c994;
    --ph-warm: #c9a272;
    --ph-grey: #b9b4ae;
    --ph-dark: #5a4d45;
    --ph-gold: #e4b97e;
    --ph-olive: #6a6a5e;
    --ph-tan: #b98e5e;
    --ph-bird: #8fbf4a;
    --ph-white: #e9e4de;
  }
  html, body {
    margin: 0;
    padding: 0;
    width: 1105px;
    height: 1200px;
    overflow: hidden;
    background: var(--paper);
  }
  .card {
    position: relative;
    width: 1105px;
    height: 1200px;
    box-sizing: border-box;
    border: 1px solid var(--edge);
    background: var(--paper);
    overflow: hidden;
  }
  .fold-line {
    position: absolute;
    left: 0;
    top: 576px;
    width: 100%;
    height: 1px;
    background: var(--edge);
  }
  .brand-name {
    position: absolute;
    left: 459px;
    top: 62px;
    width: 200px;
    transform: rotate(180deg);
    text-align: center;
    font-family: "Arimo", sans-serif;
    font-weight: 700;
    font-size: 15px;
    line-height: 1.25;
    letter-spacing: 0.5px;
    color: var(--brand-brown);
    text-transform: uppercase;
  }
  .corner-wash {
    position: absolute;
    left: 0;
    top: 0;
    width: 1105px;
    height: 1200px;
  }
  .animal {
    position: absolute;
    border-radius: 40%;
    opacity: 0.85;
  }
  .animal--chicken { left: 78px;  top: 612px; width: 92px;  height: 153px; background: var(--ph-warm); }
  .animal--rabbit  { left: 197px; top: 608px; width: 88px;  height: 151px; background: var(--ph-grey); }
  .animal--ferret  { left: 287px; top: 620px; width: 162px; height: 115px; background: var(--ph-dark); }
  .animal--snake   { left: 457px; top: 642px; width: 145px; height: 72px;  background: var(--ph-gold); }
  .animal--rat     { left: 620px; top: 633px; width: 158px; height: 89px;  background: var(--ph-olive); }
  .animal--lizard  { left: 786px; top: 633px; width: 168px; height: 89px;  background: var(--ph-tan); }
  .animal--parrots { left: 338px; top: 752px; width: 145px; height: 128px; background: var(--ph-bird); }
  .animal--hamster { left: 517px; top: 746px; width: 125px; height: 91px;  background: var(--ph-white); }
  .message {
    position: absolute;
    left: 47px;
    top: 883px;
    margin: 0;
    font-family: "Arimo", sans-serif;
    font-weight: 400;
    font-size: 40px;
    line-height: 49px;
    color: var(--orange-text);
    white-space: nowrap;
  }
  .condolence {
    position: absolute;
    left: 63px;
    top: 990px;
    margin: 0;
    font-family: "Lobster", cursive;
    font-weight: 400;
    font-size: 40px;
    line-height: 50px;
    color: var(--green-text);
    white-space: nowrap;
  }
</style>
</head>
<body>
  <main class="card">
    <svg class="corner-wash" viewBox="0 0 1300 1412" preserveAspectRatio="none" role="img" aria-label="Decorative sweep of soft green and peach stripes rising to the lower right corner">
      <defs>
        <linearGradient id="washFill" x1="0" y1="1" x2="1" y2="0.55">
          <stop offset="0" stop-color="var(--wash-pale)"/>
          <stop offset="0.5" stop-color="var(--wash-green)"/>
          <stop offset="1" stop-color="var(--wash-peach)"/>
        </linearGradient>
      </defs>
      <path d="M0,1290 C420,1272 930,1150 1300,676 L1300,1412 L0,1412 Z" fill="url(#washFill)"/>
    </svg>

    <div class="brand-name">Meadowbrook<br>Pet Hospital</div>

    <div class="fold-line"></div>

    <div class="animal animal--chicken" role="img" aria-label="Photo of a golden hen"></div>
    <div class="animal animal--rabbit" role="img" aria-label="Photo of a grey and white rabbit"></div>
    <div class="animal animal--ferret" role="img" aria-label="Photo of a dark ferret lying down"></div>
    <div class="animal animal--snake" role="img" aria-label="Photo of a coiled orange corn snake"></div>
    <div class="animal animal--rat" role="img" aria-label="Photo of a dark grey rat"></div>
    <div class="animal animal--lizard" role="img" aria-label="Photo of a bearded dragon lizard"></div>
    <div class="animal animal--parrots" role="img" aria-label="Photo of two parrots on a perch"></div>
    <div class="animal animal--hamster" role="img" aria-label="Photo of a white hamster"></div>

    <p class="message">Goodbyes are Not Forever.<br>Goodbyes are Not the End.</p>
    <p class="condolence">So Sorry for Your Loss.</p>
  </main>
</body>
</html>
```